Pet Shop Website

website will need to have the following features:
• Photo Galleries of each species (Dogs, Cats, Birds, Fish, Reptiles, Rabbits) in a light box popup
o Each species may have several different categories for example:
 Fish
• Marine fish
• Fresh water
• tropical
• Cichlid
• Information Fact sheets of each species – Downloaded as a pdf which can be either
o Care Sheets
o Training Sheets
• Members Area
o Username (Email Address) & Password login
o New signups
o Exclusive Member Deals
o Newsletter options

The front page must be very simple (for example lumavest.com.au) contain the following:
• Product of the week - which can be purchased online
o Short details
o Cost
• Pet Club Sign up picture
• Animal of the week/month
• Contact Phone Number and addresses of the stores
• A jQuery slideshow (Images could include stores, pets etc…)
The main page MUST keep simple. We do not want it cluttered.

Inner Page
The animals / reptile page will need to have:
• Short description of the species
• Photo Galleries
• A list of what is in stock and the list needs to clearly be sorted by each store (Use of Tabs maybe).
• Facts sheets / Info sheets
The type of website ideas (not the type of look that we are necessary after) is and the sort of content that we want to offer are as follows:

http://www.scalenook.com.au/
http://www.brindlecovepaws.com.au/
http://www.thefurrowden.com.au
http://www.tailtown.net.au

Colour in the new website:
Blue
Red
Grey
Yellow

Original site:

http://www.critterglow.com.au
Updates

Hi Guys,

We had feedback from the client and they would like to see a few dark designs.

Thanks                                   

Reason: We would like to reopen this contest back up for a further week

Target Market(s)

Targeting animal lovers

Industry/Entity Type

Store

Requirements
Should not have
• Alter the logo in anyway

```html
<!DOCTYPE html>
<html lang="en">
<head>
<meta charset="utf-8">
<title>Critter Glow</title>
<link rel="stylesheet" href="https://fonts.googleapis.com/css2?family=Comfortaa:wght@400;700&family=Signika:wght@300;400;600&family=Open+Sans:wght@400;600&display=swap">
<style>
:root{
  --red:#c1161c;
  --blue:#2f9fd8;
  --ink:#333;
  --white:#fff;
  --panel:#2b2b2b;
  --panel-edge:#3b3b3b;
  --muted:#7c7c7c;
}
*{box-sizing:border-box;margin:0;padding:0}
html,body{width:1123px;height:1200px;overflow:hidden;background:#000}
.stage{width:1200px;height:1282px;position:relative;transform:scale(.93583);transform-origin:0 0;font-family:"Signika",sans-serif;color:var(--white)}
.backdrop{position:absolute;inset:0;background:
  radial-gradient(ellipse at 85% 35%,#8a6a58 0%,transparent 45%),
  radial-gradient(ellipse at 15% 20%,#8f9bb0 0%,transparent 50%),
  linear-gradient(180deg,#9aa3b5 0%,#6d6270 30%,#5a4538 55%,#1b1512 72%,#000 80%)}
.abs{position:absolute}
.logo{left:146px;top:30px;font-size:34px;font-weight:600;color:#f3c832;letter-spacing:1px}
.toplinks{right:157px;top:4px;font-size:14px}
.toplinks span{margin:0 8px}
.phone{left:866px;top:36px}
.numbers{left:910px;top:36px;font-size:18px;line-height:22px;letter-spacing:.5px}
.nav{left:110px;top:98px;width:980px;height:51px;background:linear-gradient(#3d3d3d,#1c1c1c);border-radius:4px 4px 0 0;display:flex;align-items:center}
.nav a{color:var(--white);text-decoration:none;font-size:16px;font-weight:300;padding:0 28px;border-right:1px solid #444;line-height:36px}
.nav a:first-child{padding-left:22px}
.nav a:last-of-type{border-right:none}
.search{margin-left:auto;margin-right:10px;width:250px;height:30px;background:var(--white);border-radius:4px;color:#999;font-size:14px;font-weight:300;padding:0 16px;display:flex;align-items:center;justify-content:space-between}
.hero{left:110px;top:148px;width:980px;height:414px;overflow:hidden;background:linear-gradient(90deg,#f6dedb 0%,#f3e1dc 40%,#c8784b 62%,#e9d6cc 80%,#d8403a 100%)}
.hero-copy{left:35px;top:78px;width:560px;font-family:"Comfortaa",sans-serif}
.hero-copy .l1{font-size:30px;color:var(--red);white-space:nowrap}
.hero-copy .l2{font-size:41px;color:var(--red);line-height:46px;white-space:nowrap}
.hero-copy .l2 span{color:var(--ink)}
.hero-copy p{font-family:"Open Sans",sans-serif;font-size:15px;line-height:19.5px;color:var(--ink);margin:8px 0 0 7px;width:385px}
.btn-explore{display:block;margin:15px 0 0 7px;width:142px;height:37px;background:linear-gradient(#d9161d,#a80e12);border-radius:3px;font-family:"Signika",sans-serif;font-size:18px;color:var(--white);text-align:center;line-height:37px;box-shadow:0 1px 0 #7b0a0d}
.dots{left:25px;top:385px;display:flex;gap:5px}
.dots i{width:15px;height:15px;border-radius:50%;background:var(--white)}
.dots i:first-child{width:18px;height:18px;margin-top:-1px;background:#1f78c6}
.products{left:110px;top:590px;width:980px;height:366px;border:1px solid #444;border-radius:4px;overflow:hidden;background:linear-gradient(rgba(40,30,25,.35),rgba(25,25,25,.9) 70%,#232323)}
.products h2{height:41px;background:linear-gradient(#fafafa,#d9d9d9);color:#222;font-weight:400;font-size:18px;line-height:41px;padding-left:24px}
.col{position:absolute;top:57px;width:292px}
.col h3{font-size:16px;font-weight:600;margin-left:8px}
.photo{margin-top:11px;height:155px;border:1px solid #ddd;border-radius:2px;position:relative}
.price{position:absolute;right:-8px;top:111px;width:68px;height:28px;background:var(--blue);font-size:15px;font-weight:600;text-align:center;line-height:28px}
.col p{font-family:"Open Sans",sans-serif;font-size:11.5px;line-height:14px;color:#ddd;margin:12px 0 0 8px;width:290px}
.btns{display:flex;gap:9px;margin:16px 0 0 8px}
.btn{height:26px;padding:0 9px;font-size:12px;font-weight:600;line-height:26px;border-radius:3px}
.btn.light{background:linear-gradient(#fff,#cfcfcf);color:#333}
.btn.red{background:linear-gradient(#d9161d,#a80e12)}
.club{background:linear-gradient(90deg,#f4eee8,#ece2d6);overflow:hidden}
.club .pup{position:absolute;left:0;top:0;width:110px;height:100%;background:linear-gradient(#a57b52,#d8cfc6)}
.club .offer{position:absolute;right:14px;top:28px;color:#222;font-size:14px;font-weight:600}
.club .join{position:absolute;right:14px;top:44px;color:#2d55b8;font-size:46px;font-weight:600;line-height:40px;text-align:right;letter-spacing:-1px}
.footer{left:110px;top:981px;width:980px;height:242px;background:var(--panel);border:1px solid var(--panel-edge);border-bottom:none;border-radius:3px 3px 0 0}
.footer h4{position:absolute;top:20px;font-size:18px;font-weight:300}
.map{position:absolute;left:31px;top:56px;width:294px;height:141px;border:2px solid #ccc;background:linear-gradient(135deg,#e6e1d4,#d9dcc7 50%,#ece6d6)}
.store{position:absolute;top:78px;font-family:"Open Sans",sans-serif;font-size:13.5px;line-height:20px;color:var(--muted)}
.field{position:absolute;left:752px;width:182px;height:27px;background:#1b1b1b;border:1px solid #444;border-radius:3px;font-size:12px;color:#999;padding:5px 10px;font-family:"Open Sans",sans-serif}
.subscribe{position:absolute;left:753px;top:186px;width:75px;height:28px;background:linear-gradient(#b8dd6a,#8fbd3c);color:#2c3a10;font-size:11px;text-align:center;line-height:28px;border-radius:2px}
.bottombar{left:0;top:1221px;width:1200px;height:40px;border-top:1px solid #2a2a2a;background:#151515;font-family:"Open Sans",sans-serif;font-size:12px;color:#999}
.bottombar .copy{position:absolute;left:141px;top:13px}
.bottombar .links{position:absolute;right:135px;top:13px}
.bottombar .links span{margin:0 5px}
</style>
</head>
<body>
<div class="stage">
  <div class="backdrop" role="img" aria-label="Blurred photo of a happy dog as page background"></div>

  <div class="abs logo">Critter Glow</div>
  <div class="abs toplinks">Sign In<span>|</span>Contact Us</div>
  <svg class="abs phone" width="38" height="44" viewBox="0 0 38 44"><path d="M9 2c3-2 6 0 7 3l2 7c1 3-1 5-3 6l-2 1c1 5 4 10 8 13l2-1c2-2 5-2 7 0l5 5c2 2 2 5-1 7-4 3-10 2-15-3C9 34 3 22 4 12 4 7 6 4 9 2z" fill="#111"/></svg>
  <div class="abs numbers">1-800-555-0142<br>1-800-555-0187</div>

  <nav class="abs nav">
    <a>Home</a><a>About Us</a><a>Pets</a><a>Contact Us</a>
    <div class="search">Search Pet
      <svg width="18" height="18" viewBox="0 0 18 18"><circle cx="10" cy="7" r="5.5" fill="none" stroke="#333" stroke-width="1.6"/><path d="M6 11l-4.5 4.5" stroke="#333" stroke-width="1.8"/></svg>
    </div>
  </nav>

  <section class="abs hero" role="img" aria-label="Slideshow photo of a sleeping spaniel puppy on a red cushion">
    <div class="abs hero-copy">
      <div class="l1">Welcome to the</div>
      <div class="l2">world of <span>Critter Glow</span></div>
      <p>Lorem ipsum dolor sit amet, consectetuer adipiscing elit, sed diam nonummy nibh euismod tincidunt ut laoreet dolore magna aliquam erat volutpat. Ut wisi enim ad minim.</p>
      <div class="btn-explore">Explore Now</div>
    </div>
    <div class="abs dots"><i></i><i></i><i></i><i></i></div>
  </section>

  <section class="abs products">
    <h2>Latest Products</h2>
    <div class="col" style="left:17px">
      <h3>Animal of the Month</h3>
      <div class="photo" role="img" aria-label="Photo of a white and ginger kitten" style="background:linear-gradient(90deg,#e8e2dc,#f2ede8 50%,#d9c9c0)"><div class="price">$ 90.0</div></div>
      <p>Lorem ipsum dolor sit amet, consectetuer adipisc elitiam nonummy nibh.</p>
      <div class="btns"><div class="btn light">VIEW DETAIL</div><div class="btn red">ADD TO CART</div></div>
    </div>
    <div class="col" style="left:343px">
      <h3>Product of the Week</h3>
      <div class="photo" role="img" aria-label="Photo of a beagle puppy running on grass" style="background:linear-gradient(#5f8a34,#7fa848 50%,#4f7a2a)"><div class="price">$ 90.0</div></div>
      <p>Lorem ipsum dolor sit amet, consectetuer adipisc elitiam nonummy nibh.</p>
      <div class="btns"><div class="btn light">VIEW DETAIL</div><div class="btn red">ADD TO CART</div></div>
    </div>
    <div class="col" style="left:670px">
      <h3>Pet Club Sign Up</h3>
      <div class="photo club">
        <div class="pup" role="img" aria-label="Photo of a beagle puppy"></div>
        <div class="offer">LIMMITED OFFER</div>
        <div class="join">Join Pet<br>Club</div>
      </div>
      <p>Join Pet club Limited time offer and win Exclusive prizes.</p>
      <div class="btns"><div class="btn red">JOIN PET CLUB</div></div>
    </div>
  </section>

  <footer class="abs footer">
    <h4 style="left:31px">Shop Local</h4>
    <div class="map" role="img" aria-label="Street map showing the local store location"></div>
    <h4 style="left:357px">Out Stores</h4>
    <div class="store" style="left:358px">Shop 4 / 220 Harbour Rd<br>WESTBROOK W.A 6199<br><br>Phone: (08) 5550 1970<br>Fax: (08) 5550 1960</div>
    <div class="store" style="left:556px">Unit 3 / 18 Meadow Lane<br>FERNVALE W.A 6198<br><br>Phone: (08) 5550 6619<br>Fax: (08) 5550 6613</div>
    <h4 style="left:749px">Customer Feedback</h4>
    <div class="field" style="top:57px">Name</div>
    <div class="field" style="top:94px">Email</div>
    <div class="field" style="top:132px;height:45px">Message</div>
    <div class="subscribe">Subscribe</div>
  </footer>

  <div class="abs bottombar">
    <div class="copy">Copyright. Critter Glow. All Rights Reserved.</div>
    <div class="links">Home<span>|</span>About Us<span>|</span>Pets<span>|</span>Contact US</div>
  </div>
</div>
</body>
</html>
```